Flyer Tally Your Ledger Free

Hi
Can you please design me a DL Flyer for: Tally Your Ledger Free
Info:
Starting a new Business ?
Want to save on bookkeeping fees for your existing business?

You can now save 1000's off bookkeeping fees by Doing it Yourself.

Using our Bookkeeper software you simply key in the information as you go.

We offer one on one training, backup and support.
We can assist you with BAS Preparation and Payrol Advice.

Add Modules as required:
Point of Sale Module
Jobs Management Module
Website Intergration Module

Fee set up assistance and training.

Lets get the ball rolling: 1300 642 815
www.tylfr.com.au
admin@tylfr.com.au (use the logo thing you made)

Target Market(s)

Small Business

Colors
ec1f27
f04a50
f59296
fcdcdc
ffffff

Requirements
Nice to have
• image/s related to bookkeeping

```html
<!DOCTYPE html>
<html lang="en">
<head>
<meta charset="utf-8">
<title>Tally Your Ledger Free – DL Flyer</title>
<link href="https://fonts.googleapis.com/css2?family=Montserrat:wght@400;500;700;800&family=Roboto:wght@400;500&display=swap" rel="stylesheet">
<style>
:root{
  --red:#ec1f27;
  --red-deep:#c42a1a;
  --red-soft:#f04a50;
  --panel:#f1f1f1;
  --ink:#222;
  --grey-ink:#444;
  --white:#fff;
  --stage:#2a0003;
}
*{margin:0;padding:0;box-sizing:border-box}
html,body{width:1200px;height:857px;overflow:hidden;background:var(--stage)}
.flyer{position:absolute;left:410px;top:25px;width:380px;height:806px;background:var(--white);overflow:hidden;font-family:"Roboto",sans-serif;color:var(--ink)}
.hero-photo{position:absolute;left:0;top:0;width:380px;height:320px;background:linear-gradient(135deg,#d9d6d2 0%,#8a7f78 40%,#cfd6dc 70%,#eef0f2 100%)}
.waves{position:absolute;left:0;top:0;width:380px;height:806px}
.headline{position:absolute;left:40px;top:256px;font-family:"Montserrat",sans-serif;font-weight:800;font-size:30px;line-height:31px;color:var(--white);letter-spacing:.5px}
.subline{position:absolute;left:39px;top:357px;font-family:"Montserrat",sans-serif;font-size:11.5px;line-height:18px;color:var(--white)}
.save-frame{position:absolute;left:27px;top:438px;width:326px;height:57px;border:1px solid var(--red)}
.save-lead{position:absolute;left:0;top:424px;width:380px;text-align:center;font-size:15px}
.save-lead span,.save-tail span{background:var(--white);padding:0 14px}
.save-title{position:absolute;left:0;top:448px;width:380px;text-align:center;font-family:"Montserrat",sans-serif;font-weight:800;font-size:31px;color:var(--red);letter-spacing:.5px}
.save-tail{position:absolute;left:0;top:482px;width:380px;text-align:center;font-size:15px}
.save-tail span{padding:0 6px}
.info-panel{position:absolute;left:29px;top:514px;width:323px;height:152px;background:var(--panel)}
.points{position:absolute;left:0;top:10px;width:323px;text-align:center;font-size:9.8px;line-height:13px;list-style:none;color:var(--ink)}
.points li{margin-bottom:3px}
.modules-title{position:absolute;left:0;top:80px;width:323px;text-align:center;font-family:"Montserrat",sans-serif;font-weight:800;font-size:12.5px;letter-spacing:.3px}
.modules{position:absolute;left:9px;top:102px;display:flex;gap:7px}
.module{width:97px;height:41px;background:var(--red);color:var(--white);font-family:"Montserrat",sans-serif;font-weight:700;font-size:9px;line-height:12px;letter-spacing:.4px;display:flex;align-items:center;justify-content:center;text-align:center}
.fee-note{position:absolute;left:0;top:685px;width:380px;text-align:center;font-family:"Montserrat",sans-serif;font-weight:800;font-size:16.5px;line-height:17px;color:var(--grey-ink);letter-spacing:.5px}
.brand{position:absolute;left:22px;top:752px;display:flex;align-items:center;gap:7px;font-family:"Montserrat",sans-serif;font-weight:700;font-size:12.5px;color:var(--white)}
.brand-dot{width:12px;height:12px;border-radius:50%;background:var(--white)}
.contacts{position:absolute;left:213px;top:736px;list-style:none;font-family:"Montserrat",sans-serif;font-weight:500;font-size:11px;color:var(--white)}
.contacts li{display:flex;align-items:center;gap:6px;height:17.5px}
.contacts svg{width:11px;height:11px}
</style>
</head>
<body>
<main class="flyer">
  <div class="hero-photo" role="img" aria-label="Photo of two colleagues smiling at a laptop in a bright office"></div>

  <svg class="waves" viewBox="0 0 380 806" aria-hidden="true">
    <defs>
      <linearGradient id="redFlow" x1="0" y1="0" x2="1" y2="0">
        <stop offset="0" stop-color="#c42a1a"/>
        <stop offset="1" stop-color="#ec1f27"/>
      </linearGradient>
    </defs>
    <path d="M0 232 C70 220 140 196 200 212 C260 228 300 300 380 306 L380 320 L0 320 Z" fill="#fff"/>
    <path d="M0 240 C70 228 140 206 200 220 C262 236 300 300 380 314 L380 355 C300 390 220 414 140 414 C80 414 30 402 0 392 Z" fill="url(#redFlow)"/>
    <path d="M0 682 C80 662 140 660 190 664 C260 670 320 660 380 652 L380 806 L0 806 Z" fill="url(#redFlow)"/>
    <path d="M0 674 C80 710 140 730 190 730 C250 730 320 706 380 672 L380 640 L0 640 Z" fill="#fff"/>
  </svg>

  <h1 class="headline">STARTING<br>A NEW<br>BUSINESS?</h1>
  <p class="subline">Want to save on bookkeeping fees<br>for your existing business?</p>

  <div class="save-frame"></div>
  <p class="save-lead"><span>You can now</span></p>
  <p class="save-title">SAVE 1000'S OFF</p>
  <p class="save-tail"><span>bookkeeping fees by Doing it Yourself.</span></p>

  <section class="info-panel">
    <ul class="points">
      <li>• Using our Bookkeeper software you simply key<br>in the information as you go.</li>
      <li>• We offer one on one training, backup and support.</li>
      <li>• We can assist you with BAS Preparation and Payrol Advice.</li>
    </ul>
    <h2 class="modules-title">ADD MODULES AS REQUIRED</h2>
    <div class="modules">
      <div class="module">POINT OF<br>SALE MODULE</div>
      <div class="module">JOBS<br>MANAGEMENT<br>MODULE</div>
      <div class="module">WEBSITE<br>INTERGRATION<br>MODULE</div>
    </div>
  </section>

  <p class="fee-note">FEE SET UP ASSISTANCE<br>AND TRAINING.</p>

  <div class="brand"><span class="brand-dot"></span>Tally Your Ledger Free</div>

  <ul class="contacts">
    <li><svg viewBox="0 0 12 12"><circle cx="6" cy="6" r="6" fill="#fff"/><path d="M3.6 3.2l1.2-.4.7 1.5-.7.6c.4.8 1 1.4 1.8 1.8l.6-.7 1.5.7-.4 1.2C6.2 8 4 5.8 3.6 3.2z" fill="#ec1f27"/></svg>1300 642 815</li>
    <li><svg viewBox="0 0 12 12"><circle cx="6" cy="6" r="6" fill="#fff"/><circle cx="6" cy="6" r="3.6" fill="none" stroke="#ec1f27" stroke-width=".8"/><path d="M2.4 6h7.2M6 2.4v7.2M4.4 3c-1 2-1 4 0 6M7.6 3c1 2 1 4 0 6" stroke="#ec1f27" stroke-width=".6" fill="none"/></svg>www.tylfr.com.au</li>
    <li><svg viewBox="0 0 12 12"><circle cx="6" cy="6" r="6" fill="#fff"/><rect x="3" y="4" width="6" height="4.2" fill="none" stroke="#ec1f27" stroke-width=".8"/><path d="M3 4l3 2.4L9 4" fill="none" stroke="#ec1f27" stroke-width=".8"/></svg>admin@tylfr.com.au</li>
  </ul>
</main>
</body>
</html>
```